Zolnik Radio Web

Radio Station web site to include but not limited:

- About US (company profile)
- Now playing (from our streaming server link)
- Upcoming events with a possibility to have photos for advertisement purpose, etc...
- Language switch from Russian to English

- Member section:
Login module (with new user name and password, forgot password, etc...)
Login module with Chatterly details
Request a song
LIKE feature with Chatterly...

- Social links: (along with Chatterly LIKE)
Send page to a friend
share / chatterly share
Chat section where all logged users can chat in the same room.

- Contact us (Radio email ID )
- TabPro - MuzPod compatible

2 Websites were found to match the design that we re looking for:
http://www.vekrana.com and
http://tomarpelvin.com

The site colors shall be matching and ongoing with our logo colors and designs as well.

Thanks,
Zolnik Radio Team

Industry/Entity Type

Radio

Requirements
Must have
• Chatterly Login
Chatterly LIKE
Users Chat Section
Language Switch
TabPro - MuzPod compatible
Nice to have
• Less pages switch. Initial shall be to switch from russian to english (or EN to RU) but the less pages we flip, the better. (except pop ups for log in, request a song, etc...)

```html
<!DOCTYPE html>
<html lang="en">
<head>
<meta charset="utf-8">
<title>Zolnik Radio</title>
<link rel="stylesheet" href="https://fonts.googleapis.com/css2?family=Ubuntu:wght@400;500;700&family=Arimo:wght@400;700&family=Carlito&display=swap">
<style>
:root{
  --night:#0b0d14;
  --deep:#0d2f66;
  --panel:#12427f;
  --panel-light:#1b5aa3;
  --sky:#5fa6e4;
  --sun:#f3a826;
  --gold:#f7b52a;
  --amber:#f8c42e;
  --ink:#0f2244;
  --white:#ffffff;
  --text-blue:#8fc0ee;
}
*{box-sizing:border-box;margin:0;padding:0}
html,body{width:1200px;height:952px;overflow:hidden}
body{position:relative;background:var(--night);font-family:"Arimo",Arial,sans-serif;color:var(--white)}
.backdrop{position:absolute;left:0;top:0;width:1200px;height:861px;
  background:
   radial-gradient(ellipse 200px 160px at 60px 600px,rgba(20,30,60,.9),transparent),
   radial-gradient(ellipse 220px 200px at 1150px 700px,rgba(190,110,40,.55),transparent),
   linear-gradient(180deg,#3b58b0 0,#4a66c0 300px,#3a4f93 600px,#5a4a50 861px)}
.topbar{position:absolute;left:0;top:0;width:1200px;height:100px;background:linear-gradient(180deg,#05070d,#0e1530)}
.sun-disc{position:absolute;left:660px;top:106px;width:526px;height:526px;border-radius:50%;background:radial-gradient(circle,#f6b63a 0,var(--sun) 70%,#e49a20 100%)}
.brand{position:absolute;left:159px;top:22px;width:162px;height:162px;border-radius:50%;background:radial-gradient(circle at 40% 35%,#1c5fb0,#0b3270);display:flex;align-items:center;justify-content:center}
.brand span{font-family:"Ubuntu",sans-serif;font-weight:500;font-size:20px;color:var(--white);text-align:center;line-height:1.1}
.utility{position:absolute;top:20px;left:700px;display:flex;align-items:center;font-size:12px;color:var(--text-blue)}
.utility .chat{margin-right:24px}
.like{display:flex;align-items:center;gap:6px;margin-right:24px;font-size:10px;color:var(--white)}
.like b{background:#eef1f7;color:#3b5690;border:1px solid #9aa7c3;border-radius:2px;padding:2px 6px;font-weight:400}
.nav{position:absolute;top:67px;left:411px;display:flex;gap:19px;font-family:"Ubuntu",sans-serif;font-size:13.4px;color:var(--gold);text-transform:uppercase}
.nav .current{color:var(--white)}
.player{position:absolute;left:793px;top:147px;width:268px;font-size:11.5px;color:var(--ink)}
.player b{color:var(--white);font-weight:700}
.track{position:absolute;top:19px;left:0;width:216px;height:22px;border-radius:4px;background:linear-gradient(#3a3a3a,#111);border:1px solid #000}
.track i{position:absolute;left:10px;top:8px;width:20px;height:6px;background:var(--amber)}
.track::after{content:"";position:absolute;left:34px;right:8px;top:10px;height:2px;background:#666}
.pbtn{position:absolute;top:19px;width:22px;height:22px;border-radius:3px;background:linear-gradient(#fcd24a,#e59a12)}
.main{position:absolute;left:159px;top:200px;width:903px;height:611px;border-radius:34px 0 0 6px;background:linear-gradient(180deg,var(--panel-light),var(--panel) 60%,var(--deep));overflow:hidden}
.hero-photo{position:absolute;left:16px;top:30px;width:259px;height:394px;border-radius:120px 120px 0 0;background:linear-gradient(160deg,#2a1a1a,#c79a8c 45%,#f2e8ea 80%)}
.welcome{position:absolute;left:253px;top:43px;width:332px;height:332px;border-radius:50%;background:radial-gradient(circle,#0f3a74,#0a2b5a);border:2px solid #c29720;box-shadow:0 0 0 8px rgba(10,30,60,.5);text-align:center;padding-top:38px}
.welcome h1{font-family:"Ubuntu",sans-serif;font-weight:400;font-size:31px;line-height:1;color:var(--gold)}
.welcome h2{font-family:"Ubuntu",sans-serif;font-weight:400;font-size:37px;line-height:1.05;color:var(--white);margin-bottom:10px}
.welcome p{font-family:"Carlito",sans-serif;font-size:13px;line-height:18.5px;color:var(--text-blue);padding:0 28px}
.learn{position:absolute;left:512px;top:309px;width:78px;height:78px;border-radius:50%;background:radial-gradient(circle at 45% 35%,#ffc02e,#f08a00);border:3px solid #ffd86a;display:flex;align-items:center;justify-content:center;font-size:11px;font-weight:700}
.about{position:absolute;left:20px;top:455px;width:338px;font-family:"Carlito",sans-serif;font-size:13px;line-height:18.5px;text-align:justify}
.request{position:absolute;left:377px;top:457px;width:221px;height:128px;border-radius:8px;background:linear-gradient(180deg,#1e73c9,#0b2f7a 65%,#05102a);padding:20px 16px}
.request span{display:block;font-family:"Ubuntu",sans-serif;font-size:40px;line-height:34px;color:var(--gold)}
.request span+span{color:var(--white)}
.click{position:absolute;left:539px;top:524px;width:68px;height:68px;border-radius:50%;background:radial-gradient(circle at 45% 35%,#1d5fb4,#092a66);border:2px solid #3d78c9;display:flex;align-items:center;justify-content:center;font-size:11.5px;font-weight:700}
.login{position:absolute;left:776px;top:205px;width:281px;height:221px;background:linear-gradient(180deg,#a3cff4,var(--sky) 24%,#4b94de);border:1px solid #c8e2f9}
.login h3{font-family:"Ubuntu",sans-serif;font-weight:400;font-size:21px;color:var(--deep);padding:10px 16px;height:47px;border-bottom:1px solid #8bbde9}
.field{position:absolute;left:15px;width:243px;height:30px;background:var(--white);border:1px solid #9ab;border-radius:2px;font-size:11px;color:#888;padding:8px 9px}
.login .divider{position:absolute;left:0;right:0;top:151px;border-top:1px solid #8bbde9}
.social-sign{position:absolute;left:17px;top:180px;display:flex;align-items:center;gap:6px;font-size:11.5px;font-weight:700;color:var(--deep)}
.social-sign i{width:12px;height:12px;background:var(--deep)}
.signin{position:absolute;left:179px;top:172px;width:73px;height:27px;background:linear-gradient(#fff,#e3e3e3);border:1px solid #aaa;border-radius:2px;color:#222;font-size:11.5px;font-weight:700;text-align:center;line-height:25px}
.events{position:absolute;left:776px;top:431px;width:281px;height:376px;background:var(--amber);border:1px solid #ffe08a;padding:8px 15px;color:var(--ink);font-size:11px;line-height:14.5px}
.events h3{font-family:"Ubuntu",sans-serif;font-weight:400;font-size:21px;color:var(--deep);margin-bottom:12px}
.event-photo{width:248px;height:81px}
.e1{background:linear-gradient(120deg,#b89070,#4a2a1c 55%,#8a6a50)}
.e2{height:73px;background:linear-gradient(120deg,#8a3a14,#c4622a 50%,#5a2010)}
.event b{display:block;font-size:11.5px;margin-top:3px}
.event .date{display:block;color:#16408a;font-weight:700;font-size:11.5px;margin:2px 0}
.event .more{display:block;font-weight:700}
.event+.event{margin-top:12px}
.footer{position:absolute;left:0;top:861px;width:1200px;height:91px;background:#0e0e0e}
.footnav{position:absolute;left:159px;top:32px;display:flex;gap:16px;font-size:11.5px;color:#a0a0a0}
.copy{position:absolute;left:159px;top:50px;font-size:11px;color:#1c3a80}
.socials{position:absolute;right:142px;top:34px;display:flex;gap:9px;font-size:11px;color:#a0a0a0;align-items:center}
.socials span::before{content:"";display:inline-block;width:8px;height:8px;background:#3b7ecb;margin-right:4px}
</style>
</head>
<body>
<div class="backdrop" role="img" aria-label="Blurred blue mosaic of concert lights"></div>
<div class="topbar"></div>
<div class="sun-disc"></div>

<div class="brand"><span>Zolnik<br>Radio</span></div>

<div class="utility">
  <span class="chat">User Chat</span>
  <span class="like"><b>Like</b> 124 people like this.</span>
  <span class="lang">Language &nbsp;EN &nbsp;| &nbsp;RU</span>
</div>

<nav class="nav">
  <span class="current">Home</span><span>About Us</span><span>Now Playing</span><span>Upcoming Events</span><span>Request a Song</span><span>Login</span><span>Contact Us</span>
</nav>

<div class="player">
  <b>Now Playing</b> - Praesent lobortis erat aliquet by Jack
  <div class="track"><i></i></div>
  <div class="pbtn" style="left:220px"><svg width="22" height="22"><path d="M8 6l7 5-7 5z" fill="#111"/></svg></div>
  <div class="pbtn" style="left:246px"><svg width="22" height="22"><path d="M6 9h3l4-3v10l-4-3H6z" fill="#111"/></svg></div>
</div>

<main class="main">
  <div class="hero-photo" role="img" aria-label="Photo of a young woman listening with headphones"></div>
  <div class="welcome">
    <h1>Welcome to</h1>
    <h2>Zolnik Radio</h2>
    <p>Suspendisse convallis molestie justo non porta. Praesent lobortis erat aliquet leo mollis tempor. Nunc eu massa leo, et dapibus elit. Phasellus ornare pellentesque turpis, mattis mollis nisi pretium ut. Pellentesque ultrices turpis at orci commodo tincidunt. Donec in enim a odio aliquet laoreet. Vestibulum nec lacus ac velit ullamcorper mollis. Sed non odio augue</p>
  </div>
  <div class="learn">Learn More</div>
  <p class="about">Morbi leo sapien, iaculis nec ullamcorper vitae, consectetur vitae elit. Sed lacinia suscipit nulla quis sollicitudin. Class aptent taciti sociosqu ad litora torquent per conubia nostra, per inceptos himenaeos. Morbi laoreet pulvinar ante, at lacinia eros consequat vel. Phasellus vel neque nibh. Ut ornare massa tincidunt arcu suscipit molestie. Pellentesque id lorem vitae leo vestibulum ultricies eget ut purus. Vestibulum suscipit quam ut quam dapibus viverra.</p>
  <div class="request" role="img" aria-label="Concert crowd under stage lights"><span>Request</span><span>a Song</span></div>
  <div class="click">Click Here</div>
</main>

<section class="login">
  <h3>Login</h3>
  <div class="field" style="top:66px">User Name</div>
  <div class="field" style="top:100px">Password...</div>
  <div class="divider"></div>
  <div class="social-sign"><i></i>Sign In with Chatterly</div>
  <div class="signin">Sign In</div>
</section>

<section class="events">
  <h3>Upcoming Events</h3>
  <div class="event">
    <div class="event-photo e1" role="img" aria-label="DJ playing to a club crowd"></div>
    <b>Vestibulum ante ipsum</b>
    <span class="date">10th October 2011</span>
    Vestibulum nec lacus ac velit ullamcorper mollis. Sed non odio augue
    <span class="more">Learn More ››</span>
  </div>
  <div class="event">
    <div class="event-photo e2" role="img" aria-label="Crowd with raised hands at a concert"></div>
    <b style="margin-top:14px">Suspendisse Convallis</b>
    <span class="date">9th December 2011</span>
    Nam ut blandit arcu. Vestibulum nec lacus ac velit ullamcorper mollis.
    <span class="more">Learn More ››</span>
  </div>
</section>

<footer class="footer">
  <div class="footnav"><span>Home</span><span>About us</span><span>Now Playing</span><span>Upcoming Events</span><span>Request a Song</span><span>Login</span><span>Contact us</span></div>
  <div class="copy">copyright 2011 Zolnik Radio. All rights reserved</div>
  <div class="socials"><span>Chirpa</span><span>Vidloop</span><span>Chatterly</span><span>Linkwork</span><span>Newsdrip</span></div>
</footer>
</body>
</html>
```